postcard design for moving company

Orvane  Movers and Storage -moving company , we send postcards to potential clients that have their houses for sale. Must be a postard that is easy to read , where you can notice some deals, reason not to throw the card to junk.
family owned and operated company.
Free estimate
Flat Rate , license and insured, then we must put the zorbly and quib 5 stars.
coupons:
$50 Off for all long distance moving
1 month Free Storage for out of state moves.
5% Off for seniors nd veterans.

```html
<!DOCTYPE html>
<html lang="en">
<head>
<meta charset="utf-8">
<title>Orvane Movers and Storage – Postcard</title>
<link href="https://fonts.googleapis.com/css2?family=Hind:wght@400;500;600;700&family=Oswald:wght@500;600&display=swap" rel="stylesheet">
<style>
  :root{
    --red:#e04e50;
    --red-dark:#c9393c;
    --ink:#2b2b2d;
    --paper:#ffffff;
    --mist:#f1efee;
    --tile:#f4f4f4;
    --backdrop:#cfcfcf;
    --photo-warm-a:#e9c7b8;
    --photo-warm-b:#d7887f;
    --photo-cool-a:#8c8f96;
    --photo-cool-b:#3f434b;
  }
  *{box-sizing:border-box;margin:0;padding:0}
  html,body{width:1200px;height:904px;overflow:hidden}
  body{background:var(--backdrop);font-family:"Hind",sans-serif;position:relative}
  .card{position:absolute;width:509px;height:364px;overflow:hidden;background:var(--paper);box-shadow:0 6px 14px rgba(0,0,0,.18)}
  .card--front{left:188px;top:75px}
  .card--back{left:503px;top:465px}
  .card svg.shapes{position:absolute;inset:0}
  .abs{position:absolute}

  .brand{font-family:"Hind",sans-serif;font-weight:500;color:var(--red);line-height:1}
  .brand__name{font-size:22px;letter-spacing:-.3px}
  .brand__sub{font-size:12px;margin-top:3px;padding-left:58px}

  .headline{color:#fff;font-weight:700;font-size:15.5px;line-height:18px;text-transform:uppercase;letter-spacing:.1px}
  .ticks{list-style:none;color:#fff;font-size:10px;line-height:16px}
  .ticks li{position:relative;padding-left:11px}
  .ticks li::before{content:"";position:absolute;left:0;top:4px;width:7px;height:7px;border-radius:50%;background:#fff}
  .ticks li::after{content:"";position:absolute;left:2.2px;top:5.3px;width:2px;height:3.4px;border:solid var(--red);border-width:0 1.2px 1.2px 0;transform:rotate(45deg)}
  .ticks li.wrap{line-height:13px;padding-top:1.5px}

  .coupon{position:absolute;left:22px;width:199px;height:31px;border:1.4px solid #fff;border-radius:3px;display:flex;overflow:hidden}
  .coupon__value{width:90px;background:var(--mist);color:var(--red);font-family:"Oswald",sans-serif;font-weight:600;display:flex;flex-direction:column;align-items:center;justify-content:center;line-height:1}
  .coupon__value--big{font-size:24px}
  .coupon__value sup{font-size:10px;vertical-align:top;margin-right:2px;position:relative;top:-4px}
  .coupon__value .main{font-size:17px}
  .coupon__value .small{font-size:10px;margin-top:1px}
  .coupon__terms{flex:1;color:#fff;font-weight:700;font-size:10px;line-height:12.5px;padding:3px 0 0 7px;text-transform:uppercase;display:flex;align-items:center}

  .contact{color:#fff;font-size:12px;line-height:16px}
  .contact li{list-style:none;display:flex;align-items:center;gap:5px}
  .dot-icon{width:9px;height:9px;flex:none}

  .section-title{font-weight:700;font-size:12px;text-transform:uppercase;color:#fff;letter-spacing:.1px}
  .section-title--red{color:var(--red)}
  .ticks--back{font-size:10px;line-height:16.3px;font-weight:500}

  .address{color:var(--ink);font-size:9px;line-height:11px}
  .stamp{border:1px solid #9a9a9a;width:60px;height:61px}
  .rule{height:1px;background:#8e8e8e;width:163px;left:323px}

  .clients{display:grid;grid-template-columns:repeat(6,35px);gap:4px 4px}
  .client{width:35px;height:24px;background:#fff;border:1px solid #e2e2e2;display:flex;align-items:center;justify-content:center}
  .client span{display:block;background:#c9c9c9;border-radius:2px}

  .footer-bar{color:#fff;font-size:10.5px;display:flex;align-items:center;gap:14px}
  .footer-bar span{display:flex;align-items:center;gap:4px}
</style>
</head>
<body>

<!-- FRONT -->
<section class="card card--front" aria-label="Postcard front">
  <svg class="shapes" width="509" height="364" viewBox="0 0 509 364">
    <defs>
      <linearGradient id="familyTone" x1="0" y1="0" x2="1" y2="1">
        <stop offset="0" stop-color="#f3f0ee"/>
        <stop offset=".5" stop-color="var(--photo-warm-a)"/>
        <stop offset="1" stop-color="var(--photo-warm-b)"/>
      </linearGradient>
      <linearGradient id="crewTone" x1="0" y1="0" x2="1" y2="1">
        <stop offset="0" stop-color="var(--photo-cool-a)"/>
        <stop offset="1" stop-color="var(--photo-cool-b)"/>
      </linearGradient>
    </defs>
    <rect width="509" height="364" fill="var(--mist)"/>
    <path d="M215,0 H509 V260 L330,280 L215,230 Z" fill="url(#familyTone)" role="img" aria-label="Photo of a smiling family of three at home"/>
    <path d="M286,364 C296,300 320,280 360,270 L509,248 V364 Z" fill="var(--paper)"/>
    <path d="M292,364 C302,306 326,286 364,276 L509,256 V364 Z" fill="var(--ink)"/>
    <path d="M0,116 C40,85 95,70 150,70 C225,70 275,115 300,175 L268,364 H0 Z" fill="var(--red)"/>
    <circle cx="319" cy="218" r="76" fill="var(--paper)"/>
    <circle cx="319" cy="218" r="72" fill="url(#crewTone)" role="img" aria-label="Photo of movers loading boxes into a truck"/>
  </svg>

  <div class="abs brand" style="left:23px;top:17px">
    <div class="brand__name">Orvane Movers</div>
    <div class="brand__sub">&amp; Storage</div>
  </div>

  <h1 class="abs headline" style="left:22px;top:109px">A luxury service that<br>goes beyond the traditional<br>moving experience</h1>

  <ul class="abs ticks" style="left:22px;top:167px;width:200px">
    <li>Family owned and operated company.</li>
    <li>Free estimate</li>
    <li class="wrap">Flat Rate, license and insured, then we must put the zorbly and quib 5 stars.</li>
  </ul>

  <div class="coupon" style="top:237px">
    <div class="coupon__value coupon__value--big"><div><sup>$</sup>50 OFF</div></div>
    <div class="coupon__terms">For all long<br>distance moving</div>
  </div>
  <div class="coupon" style="top:274px">
    <div class="coupon__value"><div class="main">1 MONTH</div><div class="small">FREE STORAGE</div></div>
    <div class="coupon__terms">For out of state<br>moves</div>
  </div>
  <div class="coupon" style="top:311px">
    <div class="coupon__value coupon__value--big">5% OFF</div>
    <div class="coupon__terms">For seniors nd<br>veterans</div>
  </div>

  <ul class="abs contact" style="left:308px;top:300px">
    <li><svg class="dot-icon" viewBox="0 0 10 10"><circle cx="5" cy="5" r="5" fill="var(--red)"/><path d="M3.2,2.6 L4.2,3.6 L3.7,4.3 C4.1,5.1 4.8,5.8 5.6,6.2 L6.3,5.7 L7.3,6.7 L6.6,7.5 C4.6,7.2 2.8,5.4 2.5,3.4 Z" fill="#fff"/></svg>(555) 014-2290</li>
    <li><svg class="dot-icon" viewBox="0 0 10 10"><circle cx="5" cy="5" r="5" fill="var(--red)"/><rect x="2.5" y="3.3" width="5" height="3.6" fill="none" stroke="#fff" stroke-width=".8"/><path d="M2.5,3.3 L5,5.3 L7.5,3.3" fill="none" stroke="#fff" stroke-width=".8"/></svg>office@orvanemovers.com</li>
    <li><svg class="dot-icon" viewBox="0 0 10 10"><circle cx="5" cy="5" r="5" fill="var(--red)"/><circle cx="5" cy="5" r="2.6" fill="none" stroke="#fff" stroke-width=".7"/><path d="M2.4,5 H7.6 M5,2.4 C3.8,4 3.8,6 5,7.6 M5,2.4 C6.2,4 6.2,6 5,7.6" fill="none" stroke="#fff" stroke-width=".6"/></svg>www.orvanemovers.com</li>
  </ul>
</section>

<!-- BACK -->
<section class="card card--back" aria-label="Postcard back">
  <svg class="shapes" width="509" height="364" viewBox="0 0 509 364">
    <defs>
      <linearGradient id="teamTone" x1="0" y1="0" x2="1" y2="0">
        <stop offset="0" stop-color="#4a4d54"/>
        <stop offset="1" stop-color="#1f2125"/>
      </linearGradient>
      <linearGradient id="packTone" x1="0" y1="0" x2="1" y2="1">
        <stop offset="0" stop-color="#c9c4bd"/>
        <stop offset="1" stop-color="#7d7872"/>
      </linearGradient>
    </defs>
    <rect width="509" height="364" fill="var(--paper)"/>
    <path d="M0,0 H207 C268,40 292,100 289,200 V364 H0 Z" fill="var(--red)"/>
    <path d="M0,262 C60,228 150,218 225,248 L300,364 H0 Z" fill="var(--tile)"/>
    <path d="M255,364 L290,300 C370,268 450,262 509,240 V364 Z" fill="url(#teamTone)" role="img" aria-label="Photo of the moving crew standing in front of their truck"/>
    <path d="M0,334 H280 L294,364 H0 Z" fill="var(--ink)"/>
    <circle cx="264" cy="229" r="66" fill="var(--paper)"/>
    <circle cx="264" cy="229" r="62" fill="url(#packTone)" role="img" aria-label="Photo of movers wrapping furniture"/>
  </svg>

  <h2 class="abs section-title" style="left:22px;top:19px">Our services</h2>
  <ul class="abs ticks ticks--back" style="left:22px;top:36px">
    <li>Local Moving</li><li>Commercial Moving</li><li>Long Distance</li><li>Exclusive Division</li>
  </ul>
  <ul class="abs ticks ticks--back" style="left:141px;top:36px">
    <li>Student Moving</li><li>Fine Art &amp; Antique</li><li>Trade Show Movers</li><li>International Moving</li>
  </ul>

  <h2 class="abs section-title" style="left:22px;top:124px">Why Orvane Movers?</h2>
  <ul class="abs ticks ticks--back" style="left:22px;top:141px">
    <li>Guaranteed Price</li><li>Stellar Service</li><li>Adaptability</li><li>Expertise</li><li>Efficient</li>
  </ul>
  <ul class="abs ticks ticks--back" style="left:120px;top:141px">
    <li>Family Owned &amp; Operated</li><li>We Are Not Brokers</li><li>Safe</li><li>Reliable</li>
  </ul>

  <h2 class="abs section-title section-title--red" style="left:22px;top:255px">Some of our customer</h2>
  <div class="abs clients" style="left:22px;top:272px">
    <div class="client"><span style="width:22px;height:8px"></span></div>
    <div class="client"><span style="width:24px;height:5px"></span></div>
    <div class="client"><span style="width:8px;height:8px;border-radius:50%"></span></div>
    <div class="client"><span style="width:22px;height:6px"></span></div>
    <div class="client"><span style="width:20px;height:8px"></span></div>
    <div class="client" style="visibility:hidden"></div>
    <div class="client"><span style="width:10px;height:9px"></span></div>
    <div class="client"><span style="width:18px;height:6px"></span></div>
    <div class="client"><span style="width:16px;height:7px"></span></div>
    <div class="client"><span style="width:14px;height:9px;border-radius:50%"></span></div>
    <div class="client"><span style="width:9px;height:9px;border-radius:50%"></span></div>
    <div class="client"><span style="width:20px;height:5px"></span></div>
  </div>

  <div class="abs footer-bar" style="left:22px;top:339px">
    <span><svg class="dot-icon" viewBox="0 0 10 10"><circle cx="5" cy="5" r="5" fill="var(--red)"/><path d="M3.2,2.6 L4.2,3.6 L3.7,4.3 C4.1,5.1 4.8,5.8 5.6,6.2 L6.3,5.7 L7.3,6.7 L6.6,7.5 C4.6,7.2 2.8,5.4 2.5,3.4 Z" fill="#fff"/></svg>(555) 014-2290</span>
    <span><svg class="dot-icon" viewBox="0 0 10 10"><circle cx="5" cy="5" r="5" fill="var(--red)"/><circle cx="5" cy="5" r="2.6" fill="none" stroke="#fff" stroke-width=".7"/><path d="M2.4,5 H7.6" stroke="#fff" stroke-width=".6"/></svg>www.orvanemovers.com</span>
  </div>

  <div class="abs brand" style="left:270px;top:17px">
    <div class="brand__name">Orvane Movers</div>
    <div class="brand__sub">&amp; Storage</div>
  </div>
  <p class="abs address" style="left:292px;top:62px">214 Larkfield Ave #305, Brookvale,<br>&nbsp;NY 10099, USA</p>
  <div class="abs stamp" style="left:426px;top:22px"></div>
  <div class="abs rule" style="top:142px"></div>
  <div class="abs rule" style="top:166px"></div>
  <div class="abs rule" style="top:190px"></div>
</section>

</body>
</html>
```